Piano Tuning Company Needs a Postcard Design to Advertise Online Appointments

I need a postcard design for my piano tuning company. I help maintain my client's piano by tuning and doing minor repairs to increase the joy of playing their instrument. My website is now set up to book appointments online and I would like to offer $10 off of any service for making an appointment from our website, valid for 2014 only. The online booking application allows customers to see all openings on the calendar for the service they are looking for and sidesteps playing phone tag to set up an appointment. I would like to see designs that go well with the logo and its color scheme. The final design should communicate warmth, professionalism and a desire to maintain their beautiful instrument.

Target Market(s)

People who own pianos

Industry/Entity Type

It Company

Requirements
Must have
• larkwellkeys@brindlemail.net
• (425) 637-5104
• Try our online booking service and receive $10 off any service
• Offer only valid for 2014
Nice to have
• Definitely picture(s) of pianos. I have attached one that is also on my business card, but if a different picture(s) work better for your design, please feel free to use it.
• It might be nice to have something about "avoid playing phone tag, try our online service." Or there could be something about a piano needing to be tuned once a year, and when was the last time your piano was tuned?

```html
<!DOCTYPE html>
<html lang="en">
<head>
<meta charset="utf-8">
<title>Larkwell Keys – Tuning Postcard</title>
<link href="https://fonts.googleapis.com/css2?family=Playfair+Display:ital,wght@0,400;1,400&display=swap" rel="stylesheet">
<style>
  :root {
    --magenta-deep: #9c1a5a;
    --magenta: #c42a7a;
    --magenta-bright: #de3f8f;
    --pink-offer: #d6337d;
    --plum: #5a2048;
    --white: #ffffff;
    --photo-dark: #1d1a1a;
    --photo-warm: #b07a3c;
  }
  html, body {
    margin: 0;
    padding: 0;
    overflow: hidden;
    background: var(--white);
  }
  .postcard {
    position: relative;
    width: 1200px;
    height: 777px;
    overflow: hidden;
    background: var(--white);
    font-family: "Playfair Display", Georgia, serif;
  }
  .hero-band {
    position: absolute;
    left: 0; top: 0;
    width: 1200px;
    height: 560px;
  }
  .headline {
    position: absolute;
    left: 0; top: 66px;
    width: 1200px;
    margin: 0;
    text-align: center;
    font-style: italic;
    font-weight: 400;
    font-size: 63px;
    line-height: 80px;
    color: var(--white);
    white-space: nowrap;
  }
  .reminder {
    position: absolute;
    left: 44px; top: 258px;
    width: 400px;
    margin: 0;
    text-align: center;
    font-style: italic;
    font-size: 38px;
    line-height: 49px;
    color: var(--white);
  }
  .piano-photo {
    position: absolute;
    left: 464px; top: 188px;
    width: 654px;
    height: 429px;
    box-sizing: border-box;
    border: 3px solid var(--white);
    background:
      radial-gradient(ellipse at 30% 40%, rgba(176,122,60,0.9), rgba(176,122,60,0) 55%),
      linear-gradient(160deg, var(--photo-warm) 0%, #6b4a2a 35%, var(--photo-dark) 60%, #2b2624 100%);
  }
  .brand {
    position: absolute;
    left: 48px; top: 634px;
    display: flex;
    align-items: center;
    gap: 14px;
  }
  .brand-mark {
    width: 34px;
    height: 34px;
    background: var(--plum);
  }
  .brand-name {
    font-size: 50px;
    font-weight: 400;
    color: var(--plum);
    line-height: 1;
    white-space: nowrap;
  }
  .contact {
    position: absolute;
    left: 48px; top: 704px;
    margin: 0;
    font-size: 19px;
    line-height: 26px;
    color: var(--plum);
    white-space: nowrap;
  }
  .offer {
    position: absolute;
    left: 495px; top: 644px;
    width: 630px;
    margin: 0;
    text-align: center;
    font-style: italic;
    font-size: 29px;
    line-height: 42px;
    color: var(--pink-offer);
    white-space: nowrap;
  }
</style>
</head>
<body>
<div class="postcard">
  <svg class="hero-band" viewBox="0 0 1200 560" aria-hidden="true">
    <defs>
      <linearGradient id="bandFill" x1="0" y1="0" x2="1" y2="1">
        <stop offset="0" stop-color="#b21f68"/>
        <stop offset="0.45" stop-color="#d23584"/>
        <stop offset="1" stop-color="#8f1852"/>
      </linearGradient>
    </defs>
    <rect width="1200" height="560" fill="url(#bandFill)"/>
    <path d="M0 40 C300 -20 700 120 1200 20 L1200 0 L0 0 Z" fill="#9c1a5a" opacity="0.55"/>
    <path d="M0 170 C350 90 750 230 1200 110" stroke="#f06aa8" stroke-width="3" fill="none" opacity="0.45"/>
    <path d="M0 230 C400 150 800 300 1200 190" stroke="#f48ab9" stroke-width="2" fill="none" opacity="0.35"/>
    <path d="M0 470 C300 400 600 520 1200 420 L1200 560 L0 560 Z" fill="#a11c5e" opacity="0.45"/>
    <path d="M700 0 C850 120 1050 160 1200 260 L1200 0 Z" fill="#e0509b" opacity="0.25"/>
  </svg>

  <h1 class="headline">When your piano was tuned last time?</h1>

  <p class="reminder">If it has been<br>longer than one year,<br>schedule your next<br>tuning now.</p>

  <div class="piano-photo" role="img" aria-label="Photo of a black grand piano with its lid open and a tufted leather bench, in a warmly lit room"></div>

  <div class="brand">
    <span class="brand-mark"></span>
    <span class="brand-name">Larkwell Keys</span>
  </div>

  <p class="contact">larkwellkeys@brindlemail.net &nbsp;·&nbsp; (425) 637-5104</p>

  <p class="offer">$10 off of any service for making an appointment<br>from our website. Valid for 2014 only.</p>
</div>
</body>
</html>
```